Marlow Landscaping Landing Page

I require a landing page for my landscaping business.

My business plan revolves around hooking clients with weeding services. Not lawn herbicide sprays, but actual hand weeding and bed maintenance. I've found my niche as most people do not want to do this kind of work. From there I often upsell clients into actual hardscaping or softscaping.

I like things to be clean, concise, and to the point. Not overly flashy, but not so minimal that that it's boring. My logo is a very good example of what I like.

The business is LGBTQ owned and operated. I do not broadcast this but I feel the logo itself, along with the name is usually enough to tip people into assumption. I'm not opposed to color, but I do not want the page to scream "gay". My favourite color is yellow...

I used to be a door to door salesman so I'm doing something different where I want to do all my selling in my first meeting with the client. With this said I do not need a section for "work pictures", as I have photos of my work on my tablet, which I show the client during the consultation.

Ideally i'd like my web site to actually be just a landing page. I'd like room for all the following information within the page;

- description of services;
Weeding of Perennial and Flower Beds
Selective Pruning of Trees and Shrubs
Hedging
Landscape Construction
Landscape Design
Total Lawn Treatment Plans
Landscape Pest Control

- contact information, phone, email
Gerald Hanswick
204-731-4426
ger.hanswick@brelvanyard.com

- "free estimates" somewhere on the page that is either led to by the eye, or very easy to notice and see

- and my slogan which is "dependable, reliable, consistent"

- room for a link to my future ratewell account so they can see reviews from real people

- My Logo present

Any or all of these can be custom made graphics or simply text, whatever looks best

I do not want people to have to search for information throughout. Design it in such a way that either the eye flows naturally from one piece of information to the other, or that it's all compartmentalized neatly enough that everything is easy to find.

As I am a landscape and outdoor maintenance service I'm no opposed to images such as flowers, trees, landscaping, etc being present. However please note that my main focus and source of income comes from weeding services, everything else is bonus cash.

Many of my clients are extremely wealthy individuals who pay over $1000 for the season for me just to show up and pull weeds. So making the website appeal to wealthy people as opposed to the average joe is paramount.

I do not cut grass. Please do not have any indication on the website, either through writing or graphics that implies that I cut grass. There are enough companies doing that.

Target Market(s)

Wealthy, often elderly individuals.

Industry/Entity Type

Landscape Gardening

Coding

Coded - Design and coding required

Number of Pages Required

1 page

Font styles to use
Sans Serif

Colors

Designer to choose colors to be used in the design.

Requirements
Must have
• - description of services;
• Weeding of Perennial and Flower Beds
• Selective Pruning of Trees and Shrubs
• Hedging
• Landscape Construction
• Landscape Design
• Total Lawn Treatment Plans
• Landscape Pest Control
• - contact information, phone, email
• Gerald Hanswick
• 204-731-4426
• ger.hanswick@brelvanyard.com
• - "free estimates" somewhere on the page that is either led to by the eye, or very easy to notice and see
• - and my slogan which is "dependable, reliable, consistent"
• - room for a link to my future ratewell account so they can see reviews from real people
• - My Logo present
Nice to have
• Flowers or weeds depicted. Possibly some hardscaping and softscaping if it doesnt look too bulky and crowded.
Should not have
• grass

```html
<!DOCTYPE html>
<html lang="en">
<head>
<meta charset="utf-8">
<title>Marlow Landscaping</title>
<link rel="stylesheet" href="https://fonts.googleapis.com/css2?family=Montserrat:wght@300;400;500;600;700;800&display=swap">
<style>
  :root {
    --panel-yellow: #fef9c6;
    --frame-dash: #e4dd9e;
    --placeholder-ink: #d7d2a4;
    --accent-olive: #8f8838;
    --ink: #232323;
    --ink-soft: #5c5c5c;
    --slogan-grey: #e6e6e6;
    --rule-grey: #eeeeee;
    --icon-grey: #7d7d7d;
    --icon-soft: #c9c9c9;
    --review-red: #e63a2c;
    --white: #ffffff;
  }
  * { box-sizing: border-box; margin: 0; padding: 0; }
  html, body { width: 1200px; height: 800px; overflow: hidden; background: var(--white); }
  body { font-family: "Montserrat", sans-serif; color: var(--ink); }

  .page { position: relative; width: 1200px; height: 800px; }

  .service-panel {
    position: absolute; left: 0; top: 0; width: 484px; height: 800px;
    background: var(--panel-yellow);
  }
  .service-visual {
    position: absolute; left: 56px; top: 308px; width: 372px; height: 260px;
    border: 2px dashed var(--frame-dash);
    display: flex; flex-direction: column; align-items: center;
    padding-top: 40px;
  }
  .service-visual svg { width: 34px; height: 34px; }
  .service-visual-label {
    margin-top: 44px; text-align: center;
    font-weight: 300; font-size: 30px; line-height: 37px; letter-spacing: 0.5px;
    color: var(--placeholder-ink);
  }

  .brand { position: absolute; left: 556px; top: 54px; }
  .brand-name {
    display: flex; align-items: center; gap: 8px;
    font-weight: 500; font-size: 22px; letter-spacing: -0.3px; color: var(--ink);
    white-space: nowrap;
  }
  .brand-dot { width: 18px; height: 18px; border-radius: 50%; background: var(--ink); }
  .slogan {
    margin-top: 4px;
    font-weight: 800; font-size: 20.5px; letter-spacing: 0.3px; text-transform: uppercase;
    color: var(--slogan-grey); white-space: nowrap;
  }

  .estimate-callout {
    position: absolute; left: 540px; top: 318px;
    display: flex; align-items: center; gap: 10px;
    font-weight: 700; font-size: 12px; letter-spacing: 2px; text-transform: uppercase;
    color: var(--accent-olive); white-space: nowrap;
  }
  .estimate-mark { width: 22px; height: 3px; background: var(--accent-olive); }

  .service-copy {
    position: absolute; left: 540px; top: 360px; width: 372px; height: 195px;
    background: var(--panel-yellow);
    border: 2px dashed var(--frame-dash);
    padding: 22px 0 0 16px;
  }
  .service-list { list-style: none; }
  .service-item {
    font-size: 13px; font-weight: 500; line-height: 21px; color: var(--ink);
    white-space: nowrap;
  }
  .service-item--lead { font-weight: 700; }

  .contact { position: absolute; left: 556px; top: 584px; }
  .contact-name { font-size: 14px; font-weight: 600; line-height: 20px; }
  .contact-line { font-size: 12px; font-weight: 400; line-height: 19px; color: var(--ink-soft); }
  .contact-line a { color: inherit; text-decoration: none; }

  .copyright {
    position: absolute; left: 556px; top: 743px;
    font-size: 10.5px; font-weight: 500; letter-spacing: 0.2px; white-space: nowrap;
  }

  .review-button {
    position: absolute; left: 894px; top: 730px; width: 178px; height: 35px;
    background: var(--review-red); border-radius: 2px;
    display: flex; align-items: center; justify-content: center; gap: 8px;
    color: var(--white); text-decoration: none; white-space: nowrap;
    font-weight: 700; font-size: 10px; letter-spacing: 0.1px; text-transform: uppercase;
  }
  .review-dot { width: 12px; height: 12px; border-radius: 50%; background: var(--white); flex: none; }

  .side-rail {
    position: absolute; left: 1124px; top: 0; width: 76px; height: 800px;
    border-left: 1px solid var(--rule-grey);
  }
  .rail-icon { position: absolute; left: 25px; width: 16px; height: 16px; display: block; }
  .rail-icon svg { width: 16px; height: 16px; display: block; }
  .social-dot { display: block; width: 12px; height: 12px; margin: 2px; border-radius: 50%; background: var(--icon-soft); }
</style>
</head>
<body>
<main class="page">
  <section class="service-panel">
    <div class="service-visual" role="img" aria-label="Photo of the selected service">
      <svg viewBox="0 0 34 34" aria-hidden="true">
        <rect x="0" y="0" width="34" height="34" rx="3" fill="#d4cf93"/>
        <path d="M5 27 L13 17 L19 24 L23 20 L29 27 Z" fill="#fef9c6"/>
      </svg>
      <p class="service-visual-label">Picture of<br>Selected Service</p>
    </div>
  </section>

  <header class="brand">
    <div class="brand-name"><span class="brand-dot"></span>MARLOW LANDSCAPING</div>
    <p class="slogan">Dependable, Reliable, Consistent</p>
  </header>

  <p class="estimate-callout"><span class="estimate-mark"></span>Free Estimates</p>

  <article class="service-copy" aria-label="Services">
    <ul class="service-list">
      <li class="service-item service-item--lead">Weeding of Perennial and Flower Beds</li>
      <li class="service-item">Selective Pruning of Trees and Shrubs</li>
      <li class="service-item">Hedging</li>
      <li class="service-item">Landscape Construction</li>
      <li class="service-item">Landscape Design</li>
      <li class="service-item">Total Lawn Treatment Plans</li>
      <li class="service-item">Landscape Pest Control</li>
    </ul>
  </article>

  <address class="contact" style="font-style:normal">
    <p class="contact-name">Gerald Hanswick</p>
    <p class="contact-line"><a href="tel:2047314426">204-731-4426</a></p>
    <p class="contact-line"><a href="mailto:ger.hanswick@brelvanyard.com">ger.hanswick@brelvanyard.com</a></p>
  </address>

  <footer>
    <p class="copyright">© 2017 Marlow Landscaping Inc.</p>
    <a class="review-button" href="#"><span class="review-dot"></span>Review us on Ratewell</a>
  </footer>

  <nav class="side-rail" aria-label="Quick links">
    <a class="rail-icon" href="#" style="top:58px" aria-label="About">
      <svg viewBox="0 0 16 16"><circle cx="8" cy="8" r="8" fill="var(--icon-grey)"/><rect x="7" y="7" width="2" height="5" fill="#fff"/><circle cx="8" cy="4.8" r="1.1" fill="#fff"/></svg>
    </a>
    <a class="rail-icon" href="#" style="top:91px" aria-label="Email">
      <svg viewBox="0 0 16 16"><rect x="0.5" y="2.5" width="15" height="11" rx="1" fill="var(--icon-grey)"/><path d="M2 4.5 L8 8.5 L14 4.5" fill="none" stroke="#fff" stroke-width="1.3"/></svg>
    </a>
    <a class="rail-icon" href="#" style="top:677px" aria-label="Social page one"><span class="social-dot"></span></a>
    <a class="rail-icon" href="#" style="top:711px" aria-label="Social page two"><span class="social-dot"></span></a>
    <a class="rail-icon" href="#" style="top:745px" aria-label="Favourite">
      <svg viewBox="0 0 16 16"><path d="M8 14.5 L2 8.6 C0.2 6.8 0.6 3.6 3 2.6 C4.8 1.9 6.7 2.6 8 4.2 C9.3 2.6 11.2 1.9 13 2.6 C15.4 3.6 15.8 6.8 14 8.6 Z" fill="var(--icon-soft)"/></svg>
    </a>
  </nav>
</main>
</body>
</html>
```